Stationary/business card/envelope design for Hollowmere Dentalcare

We are located in the foothills of the sierra nevada mountains. We are looking for a beautiful classy modern stationary. We need evelopes and business card design all to flow seamlessly. Envelope design.

Additional office address 8614 Westgate Ct., Suite B, Auburn, CA 95847 Phone: pending Fax: pending.

3 different Drs on each business card:
Marla J. Osgood, DDS
Tova R. Osgood, DDS
Rebecca M. Halvorsen, DDS

Target Market(s)

Dental patients

Industry/Entity Type

Dental

Contact Information for Business Card

Two sided. See example.

Font styles to use
Sans Serif

Requirements
Must have
• One sided business cards. Need envelope design.
Colors should match existing logo.

Marla J. Osgood, DDS
Tova R. Osgood, DDS
Rebecca M. Halvorsen, DDS

```html
<!DOCTYPE html>
<html lang="en">
<head>
<meta charset="utf-8">
<title>Hollowmere Dental Care – Stationery</title>
<link rel="stylesheet" href="https://fonts.googleapis.com/css2?family=Montserrat:wght@400;500&family=Tinos&display=swap">
<style>
  :root {
    --backdrop: #cfcfcf;
    --paper: #ffffff;
    --paper-edge: #e4e4e4;
    --folder: #333437;
    --brand-green: #2f8a45;
    --brand-blue: #4cb4d8;
    --ink: #222222;
    --muted: #555555;
  }
  * { box-sizing: border-box; margin: 0; padding: 0; }
  html, body { width: 1200px; height: 900px; overflow: hidden; }
  body { background: var(--backdrop); position: relative; font-family: "Tinos", "Times New Roman", serif; color: var(--ink); }

  .sprite { position: absolute; width: 0; height: 0; }
  .icon { width: 8px; height: 8px; fill: var(--brand-green); flex: none; }

  .sheet { position: absolute; background: var(--paper); box-shadow: 0 1px 3px rgba(0,0,0,.12); }

  /* brand mark stand-in */
  .brand { display: flex; align-items: center; gap: 8px; }
  .brand-dot { border-radius: 50%; background: var(--brand-blue); flex: none; }
  .brand-name { font-family: "Montserrat", Arial, sans-serif; font-weight: 500; color: var(--brand-green); letter-spacing: .12em; line-height: 1.35; }

  /* folder */
  .folder { left: 40px; top: 110px; width: 300px; height: 424px; background: var(--folder); }
  .folder .brand { position: absolute; left: 24px; bottom: 40px; flex-direction: column; align-items: flex-start; gap: 16px; }
  .folder .brand-dot { width: 110px; height: 110px; }
  .folder .brand-name { font-size: 17px; }

  /* letterhead */
  .letterhead { left: 370px; top: 110px; width: 330px; height: 427px; }
  .letterhead .brand { position: absolute; left: 24px; top: 22px; }
  .letterhead .brand-dot { width: 34px; height: 34px; }
  .letterhead .brand-name { font-size: 8.5px; }
  .letterhead .contact { position: absolute; left: 24px; top: 76px; font-size: 6.5px; line-height: 1.55; }
  .contact-line { display: flex; align-items: center; gap: 3px; }
  .letter-body { position: absolute; left: 118px; top: 184px; width: 180px; font-family: "Montserrat", Arial, sans-serif; font-size: 4.4px; line-height: 2.05; letter-spacing: .05em; text-align: justify; color: #333; }
  .letter-body p + p { margin-top: 6px; }

  /* envelope */
  .envelope { left: 730px; top: 110px; width: 430px; height: 216px; }
  .envelope .flap { position: absolute; left: 0; top: 0; width: 430px; height: 70px; }
  .envelope .brand { position: absolute; left: 24px; bottom: 18px; }
  .envelope .brand-dot { width: 34px; height: 34px; }
  .envelope .brand-name { font-size: 7.5px; }
  .envelope .contact { position: absolute; left: 185px; bottom: 18px; font-size: 7px; line-height: 1.5; }
  .envelope .address { position: absolute; right: 30px; bottom: 18px; font-size: 7px; line-height: 1.5; }

  /* business card */
  .card { left: 730px; top: 360px; width: 300px; height: 171px; }
  .card .doctor { position: absolute; left: 16px; top: 18px; }
  .doctor-name { font-size: 10px; color: var(--brand-green); font-variant: small-caps; letter-spacing: .03em; }
  .doctor-role { font-size: 6.5px; color: var(--muted); margin-top: 2px; }
  .card .contact { position: absolute; left: 16px; bottom: 20px; font-size: 6px; line-height: 1.6; }
  .card .brand { position: absolute; right: 16px; top: 34px; flex-direction: column; align-items: center; gap: 8px; }
  .card .brand-dot { width: 56px; height: 56px; }
  .card .brand-name { font-size: 8px; text-align: center; }
  .card .icon { width: 6px; height: 6px; }
</style>
</head>
<body>

<svg class="sprite" aria-hidden="true">
  <symbol id="i-phone" viewBox="0 0 10 10"><path d="M2 1l1.6 0 .8 2.2-1 .8a6 6 0 0 0 2.6 2.6l.8-1 2.2.8V8A1 1 0 0 1 8 9 7 7 0 0 1 1 2a1 1 0 0 1 1-1z"/></symbol>
  <symbol id="i-fax" viewBox="0 0 10 10"><path d="M3 1h4v2H3zM1 4h8v4H7.5V6.5h-5V8H1zM3 7h4v2H3z"/></symbol>
  <symbol id="i-mail" viewBox="0 0 10 10"><path d="M1 2h8v6H1zm1 1v.3L5 5.4 8 3.3V3zm0 1.5V7h6V4.5L5 6.6z"/></symbol>
  <symbol id="i-web" viewBox="0 0 10 10"><path d="M5 1a4 4 0 1 0 0 8A4 4 0 0 0 5 1zm0 1c.6.6 1 1.6 1.1 2.5H3.9C4 3.6 4.4 2.6 5 2zm-2.1 2.5H2.1a3 3 0 0 1 1.6-2.2c-.4.6-.7 1.4-.8 2.2zm0 1c.1.8.4 1.6.8 2.2a3 3 0 0 1-1.6-2.2zm1 0h2.2C6 6.4 5.6 7.4 5 8c-.6-.6-1-1.6-1.1-2.5zm3.2 0h.8a3 3 0 0 1-1.6 2.2c.4-.6.7-1.4.8-2.2zm0-1c-.1-.8-.4-1.6-.8-2.2a3 3 0 0 1 1.6 2.2z"/></symbol>
</svg>

<section class="sheet folder" aria-label="Presentation folder">
  <div class="brand">
    <span class="brand-dot"></span>
    <span class="brand-name">Hollowmere<br>Dental Care<br>Corporation</span>
  </div>
</section>

<section class="sheet letterhead" aria-label="Letterhead">
  <div class="brand">
    <span class="brand-dot"></span>
    <span class="brand-name">Hollowmere<br>Dental Care Corporation</span>
  </div>
  <address class="contact" style="font-style:normal">
    <div>8614 Westgate Ct.,</div>
    <div>Suite B, Auburn, CA 95847</div>
    <div class="contact-line"><svg class="icon"><use href="#i-phone"/></svg>(530) 214-3380</div>
    <div class="contact-line"><svg class="icon"><use href="#i-fax"/></svg>(530) 214-3391</div>
    <div class="contact-line"><svg class="icon"><use href="#i-mail"/></svg>hollowmeredentalcare@mailbox.com</div>
    <div class="contact-line"><svg class="icon"><use href="#i-web"/></svg>www.hollowmeredentalcare.com</div>
  </address>
  <div class="letter-body">
    <p>Lorem ipsum dolor sit amet, consectetur adipiscing elit. Nulla quis urna ac massa interdum tincidunt. Nulla id augue hendrerit, lorem ipsum dolor sit amet, consectetur adipiscing elit. Vivamus lacus interdum sollicitudin. Donec at imperdiet neque dapibus sed, nisl, consequat eu ligula tellus, id placerat libero vestibulum interdum. In feugiat, neque nec facilisis fermentum, magna risus tristique orci, ac tincidunt libero lorem consectetur odio. Donec vel ultrices diam, vitae cursus velit. Proin lacinia, lacus tincidunt ullamcorper aliquam, nunc dolor tempus felis, porttitor auctor tortor velit ac justo. Curabitur non bibendum est.</p>
    <p>Etiam sagittis dui quis lectus euismod laoreet. Fusce nunc ex, aliquet sed sollicitudin nec, cursus et nisi. Vivamus et nibh sapien. Pellentesque eleifend condimentum dignissim. Integer mollis sodales leo in tempor. Vivamus non purus laoreet, euismod lacus vitae, finibus dui. Suspendisse potenti. Cras convallis metus sit amet ante ornare, nec consequat vestibulum. Sed id risus sed nulla mollis efficitur. Quisque sodales ante, quis ultrices orci commodo sed. Cras mattis faucibus condimentum. Curabitur efficitur consequat augue, quis sapien ullamcorper et.</p>
    <p>Ut id convallis purus. Nulla facilisi. Sed nulla mauris, elementum nec, eleifend mattis urna. Quisque et nulla sit amet neque lacinia unt. Mauris malesuada porta sodales. Nullam gravida magna vulputate, sed cursus nulla bibendum. Aenean sed nisl ultrices, venenatis tellus sed, malesuada neque. Proin pharetra feugiat consequat. Morbi laoreet dictum nunc feugiat fermentum.</p>
  </div>
</section>

<section class="sheet envelope" aria-label="Envelope">
  <svg class="flap" viewBox="0 0 430 70" aria-hidden="true">
    <path d="M2 4 L10 58 Q12 64 20 64 L410 64 Q418 64 420 58 L428 4" fill="none" stroke="var(--paper-edge)" stroke-width="1.2"/>
  </svg>
  <div class="brand">
    <span class="brand-dot"></span>
    <span class="brand-name">Hollowmere<br>Dental Care<br>Corporation</span>
  </div>
  <div class="contact">
    <div class="contact-line"><svg class="icon"><use href="#i-phone"/></svg>(530) 214-3380</div>
    <div class="contact-line"><svg class="icon"><use href="#i-fax"/></svg>(530) 214-3391</div>
    <div class="contact-line"><svg class="icon"><use href="#i-mail"/></svg>hollowmeredentalcare@mailbox.com</div>
    <div class="contact-line"><svg class="icon"><use href="#i-web"/></svg>www.hollowmeredentalcare.com</div>
  </div>
  <div class="address">
    <div>8614 Westgate Ct.,</div>
    <div>Suite B, Auburn, CA 95847</div>
  </div>
</section>

<section class="sheet card" aria-label="Business card">
  <div class="doctor">
    <div class="doctor-name">Rebecca M. Halvorsen, DDS</div>
    <div class="doctor-role">Family &amp; Cosmetic Dentistry</div>
  </div>
  <div class="contact">
    <div>8614 Westgate Ct.,</div>
    <div>Suite B, Auburn, CA 95847</div>
    <div class="contact-line"><svg class="icon"><use href="#i-phone"/></svg>(530) 214-3380</div>
    <div class="contact-line"><svg class="icon"><use href="#i-fax"/></svg>(530) 214-3391</div>
    <div class="contact-line"><svg class="icon"><use href="#i-mail"/></svg>hollowmeredentalcare@mailbox.com</div>
    <div class="contact-line"><svg class="icon"><use href="#i-web"/></svg>www.hollowmeredentalcare.com</div>
  </div>
  <div class="brand">
    <span class="brand-dot"></span>
    <span class="brand-name">Hollowmere<br>Dental Care<br>Corporation</span>
  </div>
</section>

</body>
</html>
```